Global Summit on Thermal Peptides

We are arranging a meeting in Finland in August: THE 8th GLOBAL SUMMIT ON THERMAL PEPTIDES IN LIFE AND HEALING - CELLULAR COPING ROUTES AND CIRCUITS.

The program and speakers are included in the Word files. The basic poster arrangement could be a little bit like in the Conference:
http://events.vorelka.org/files/posters/1483956274_17-regulators-plants.pdf

Basically only the organizers and invited speakers will be listed.

We would like to have some summery maritime background of the kind provided in the stock footage. In addition, we would include some summer views from the City of Turku. We have added a few potential University Campus views in the footage folder.

Reason: There was one design that was attractive. We wanted to extend the time available to work along the approach of this design.

Target Market(s)

Scientists in the field of cell stress research

Industry/Entity Type

Management

Requirements
Must have
• There must be the logo of our home university:
• https://www.lunvik.fi/personal/media/3991/lvenglogobasic4c.jpg
• ...somewhere down on the poster, a little bit like VRKA in the example above.
• There must also be the logo of the organizing organization Tissue Strain Global Fellowship:
• http://www.tissuestrainfellows.org/?
• All text should be readable (no light text on light background and vice versa)

```html
<!DOCTYPE html>
<html lang="en">
<head>
<meta charset="utf-8">
<title>Global Summit on Thermal Peptides – Poster</title>
<link href="https://fonts.googleapis.com/css2?family=Montserrat:wght@400;500;600;700&family=Open+Sans:wght@400;600&display=swap" rel="stylesheet">
<style>
:root{
  --stage:#1b1b1b;
  --navy:#1f2f4c;
  --red:#b3232f;
  --gold:#ecd772;
  --white:#f4f4ee;
  --rule:#3a4a5e;
}
*{margin:0;padding:0;box-sizing:border-box}
html,body{width:1200px;height:938px;overflow:hidden;background:var(--stage)}
.poster{position:absolute;left:310px;top:56px;width:589px;height:833px;overflow:hidden;font-family:"Montserrat",sans-serif}
.backdrop{position:absolute;inset:0;background:linear-gradient(180deg,#f4f1de 0%,#e4e6d6 16%,#c8d2d0 24%,#9fb3bf 30%,#8ea6b2 35%,#879f86 38%,#5f8748 42%,#4a7a36 47%,#34613a 56%,#21463e 66%,#132b39 76%,#0c1a2b 88%,#0a1422 100%)}
.brand{position:absolute;display:flex;align-items:center;gap:4px;font-weight:700;font-size:8px;color:var(--red);line-height:1.1}
.brand .mark{width:9px;height:9px;background:var(--red)}
.brand-top{left:28px;top:30px}
.brand-society{right:20px;top:34px;color:var(--red)}
.brand-society .mark{border-radius:50%}
.kicker{position:absolute;top:49px;left:0;width:496px;text-align:center;font-weight:700;font-size:8.6px;line-height:11px;color:var(--red);letter-spacing:.2px}
.title{position:absolute;top:92px;left:0;width:496px;text-align:center;font-weight:600;font-size:32px;line-height:39px;color:var(--navy);letter-spacing:.5px}
.date{position:absolute;top:243px;left:0;width:496px;text-align:center;font-weight:500;font-size:17px;color:var(--red)}
.venue{position:absolute;top:272px;left:0;width:496px;text-align:center;font-weight:500;font-size:11.5px;color:var(--navy)}
.col{position:absolute;top:311px;color:var(--white)}
.col h2{font-weight:600;font-size:11px;letter-spacing:.3px;color:var(--navy);margin-bottom:3px}
.col h2.light{color:var(--white)}
.organizers{left:22px;width:124px;font-size:9.6px;line-height:14.7px}
.organizers .gold{color:var(--gold)}
.organizers .group{margin-bottom:16px}
.organizers h2{margin-top:0}
.society{position:absolute;left:16px;width:106px;text-align:center;font-weight:700;font-size:8.6px;line-height:10px;color:var(--white)}
.society-1{top:650px}
.society-2{top:697px}
.brand-bottom{position:absolute;left:30px;top:775px;width:76px;justify-content:center;color:var(--white);font-size:8.6px}
.brand-bottom .mark{background:var(--white)}
.speakers{left:146px;width:158px;font-size:9.6px;line-height:11.9px}
.speakers .label{color:var(--white);margin:6px 0 10px}
.speakers ol{list-style:none}
.speakers li .name{color:var(--gold)}
.speakers .keys{margin-bottom:10px;line-height:12.3px}
.programs{left:305px;width:280px;font-family:"Open Sans",sans-serif}
.programs h2{font-family:"Montserrat",sans-serif}
.prog-cols{display:flex;gap:9px;margin-top:4px}
.prog-col{width:135px;font-size:6.3px;line-height:7.6px}
.prog-col .blk{margin-bottom:7px}
.prog-col .hd{color:var(--gold)}
.prog-col .in{padding-left:18px}
.footer-rule{position:absolute;left:12px;right:12px;top:816px;height:1px;background:var(--rule)}
</style>
</head>
<body>
<main class="poster">
  <div class="backdrop" role="img" aria-label="Summer harbour photograph: pale sky, sea with wooded shoreline, a statue on a pedestal, flower beds and green lawn fading into dark blue"></div>

  <div class="brand brand-top"><span class="mark"></span>Lunvik<br>University</div>
  <div class="brand brand-society"><span class="mark"></span>TSGF</div>

  <p class="kicker">THE 8TH GLOBAL SUMMIT ON<br>THERMAL PEPTIDES IN LIFE AND HEALING</p>
  <h1 class="title">CELLULAR COPING<br>ROUTES<br>AND CIRCUITS</h1>
  <p class="date">August 13-17, 2017</p>
  <p class="venue">Harborline Marina Hotel Turku, Finland</p>

  <section class="col organizers">
    <div class="group">
      <h2>ORGANIZER:</h2>
      <p class="gold">Mira Halvosen<br>Lunvik University<br>Finland</p>
    </div>
    <div class="group">
      <h2 class="light">CO-ORGANIZERS:</h2>
      <p class="gold">Jonas Ekwall<br>Lunvik University<br>and University of Marhavn<br>Finland</p>
    </div>
    <div class="group">
      <p class="gold">Laurence Highfield<br>Tissue Strain Global<br>Fellowship (TSGF)<br>University of Westbrook<br>USA</p>
    </div>
    <div class="group">
      <p class="gold">Valérie Morland<br>Université Seine Nord<br>France</p>
    </div>
  </section>

  <p class="society society-1">TISSUE STRAIN GLOBAL FELLOWSHIP<br>(TSGF)</p>
  <p class="society society-2">LUNVIK<br>UNIVERSITY<br>(LU)</p>
  <div class="brand brand-bottom"><span class="mark"></span>Lunvik<br>University</div>

  <section class="col speakers">
    <h2>SPEAKERS:</h2>
    <p class="label">Keynotes (35 min + 10 min):</p>
    <ol class="keys">
      <li><span class="name">1. Anna Bertani</span>, UK</li>
      <li><span class="name">2. Marja Kettunen</span>, Denmark</li>
      <li><span class="name">3. Rick Moriyama</span>, USA</li>
      <li><span class="name">4. Peter Waldron</span>, USA</li>
    </ol>
    <p class="label">Invited speakers (20 min + 10 min):</p>
    <ol>
      <li><span class="name">1. Cristina Bonafé,</span> Brazil</li>
      <li><span class="name">2. Rochelle Bauerstein</span>, USA</li>
      <li><span class="name">3. Stuart Caldwell</span>, USA</li>
      <li><span class="name">4. Serena Carlo</span>, Italy</li>
      <li><span class="name">5. Ehud Carmeli</span>, Israel</li>
      <li><span class="name">6. Antonio Del Monte</span>, USA</li>
      <li><span class="name">7. Albena Dimova-Kostadinova</span>, UK</li>
      <li><span class="name">8. Brian C. Fairman</span>, USA</li>
      <li><span class="name">9. Carmen Galindo</span>, France</li>
      <li><span class="name">10. Linda Hendricks</span>, USA</li>
      <li><span class="name">11. Harm Kemperman</span>, The Netherlands</li>
      <li><span class="name">12. Anna-Liisa Lehtonen</span>, Finland</li>
      <li><span class="name">13. Matthias P. Maurer</span>, Germany</li>
      <li><span class="name">14. Valérie Morland</span>, France</li>
      <li><span class="name">15. Kevin A. Moretti</span>, USA</li>
      <li><span class="name">16. Kazuhiro Nakamura</span>, Japan (pending)</li>
      <li><span class="name">17. Akira Nakano</span>, Japan</li>
      <li><span class="name">18. Len Neckham</span>, USA</li>
      <li><span class="name">19. M. Bashir Omran</span>, USA</li>
      <li><span class="name">20. Jorma J. Pelkonen</span>, Finland</li>
      <li><span class="name">21. Elizabeth Ravensky</span>, USA</li>
      <li><span class="name">22. Gabriella Santini</span>, Italy</li>
      <li><span class="name">23. Michael Sherwood</span>, USA</li>
      <li><span class="name">24. Dennis J. Thielman</span>, USA</li>
      <li><span class="name">25. Jane Treadwell</span>, USA</li>
      <li><span class="name">26. Ivor Bennington</span>, USA</li>
      <li><span class="name">27. Michael Lyndon</span>, USA</li>
      <li><span class="name">28. Steve Whitcombe</span>, USA</li>
      <li><span class="name">29. Iara Linhalves</span></li>
    </ol>
  </section>

  <section class="col programs">
    <h2>TENTATIVE PROGRAMS</h2>
    <div class="prog-cols">
      <div class="prog-col">
        <div class="blk"><p class="hd">Day 1. Sunday, August 13, 2017</p><p>15:00 Registration, Poster Set-up</p><p>18:00 Welcome Get-together</p></div>
        <div class="blk"><p class="hd">Day 2. Monday, August 14, 2017</p><p>09:00 Opening of the Scientific Meeting</p><p class="in">Mira Halvosen</p><p>09:10 TSGF Awards Ceremony</p><p class="in">Laurence Highfield</p><p>09:30 Keynote 1</p><p class="in">Marja Kettunen, Denmark</p><p>10:15 Coffee/Tea</p></div>
        <div class="blk"><p class="hd">Session 1: Stress Management in Human Diseases</p><p>10:45 M. Bashir Omran, USA</p><p>11:15 Dennis Thielman, USA</p><p>11:45 Valérie Morland, France</p><p>12:15 Short talk selected from abstracts</p><p>12:30 Elizabeth Ravensky, USA</p><p>13:00 Lunch</p><p>14:00 Len Neckham, USA</p><p>14:30 Harm Kemperman, The Netherlands</p><p>15:00 Short talk selected from abstracts</p><p>15:15 Short talk selected from abstracts</p><p>15:30 Poster Session 1</p><p class="in">with Coffee/Tea</p></div>
        <div class="blk"><p class="hd">Session 2: Oxidative/Reductive Stress Responses</p><p>17:00 Michael Lyndon, USA</p><p>17:30 Ivor Bennington, USA</p><p>18:00 Short talk selected from abstracts</p><p>18:15 Albena Dimova-Kostadinova, UK</p><p>18:45 Anna-Liisa Lehtonen, Finland</p><p>19:15 Short talk selected from abstracts</p><p>19:30 Dinner</p></div>
        <div class="blk"><p class="hd">Day 3. Tuesday, August 15, 2017</p><p>09:00 Keynote 2</p><p class="in">Rick Moriyama, USA</p></div>
        <div class="blk"><p class="hd">Session 3: Stress Proteins in Aging</p><p>09:45 Ehud Carmeli, Israel</p><p>10:15 Rochelle Bauerstein, USA</p><p>10:45 Short talk selected from abstracts</p></div>
        <div class="blk"><p class="hd">Session 4: Stress Responses in Women's Health</p><p>09:45 Steve Whitcombe, USA</p><p>10:15 Iara Linhalves, USA</p><p>10:45 Short talk selected from abstracts</p><p>11:00 Coffee/Tea</p></div>
      </div>
      <div class="prog-col">
        <div class="blk"><p class="hd">Session 5: Robert Tanvier Event</p><p>&nbsp;</p><p>11:30 Antonio Del Monte, USA</p><p>12:00 TBA</p><p>12:45 TBA</p><p>13:00 TBA</p><p>13:30 Lunch &amp; TSGF Board Meeting</p><p>14:30 Free Afternoon (Dinner on your own)</p></div>
        <div class="blk"><p class="hd">Session 6: Global Regulatory Networks of Stress Genes</p><p>19:30 Brian Fairman, USA</p><p>20:00 Akira Nakano, Japan</p><p>20:30 Short talk selected from abstracts</p><p>20:45 Jorma Pelkonen, Finland</p><p>21:15 Short talk selected from abstracts</p><p>21:30-23:00 Poster Session 2</p><p class="in">with Refreshments</p></div>
        <div class="blk"><p class="hd">Day 4. Wednesday, August 16, 2017</p><p>09:00 Keynote 3</p><p class="in">Anna Bertani, UK</p></div>
        <div class="blk"><p class="hd">Session 7: Quality Control Mechanisms</p><p>09:45 Linda Hendricks, USA</p><p>10:15 Kazuhiro Nakamura, Japan</p><p>10:45 Short talk selected from abstracts</p><p>11:00 Coffee/Tea</p><p>11:30 Serena Carlo, Italy</p><p>12:00 Cristina Bonafé, Brazil</p><p>12:30 Matthias Maurer, Germany</p><p>13:00 Lunch</p></div>
        <div class="blk"><p class="hd">Session 8: Stress Proteins in Cancer</p><p>14:00 Carmen Galindo, France</p><p>14:30 Stuart Caldwell, USA</p><p>15:00 Short talk selected from abstracts</p><p>15:15 Short talk selected from abstracts</p><p>15:30 Gabriella Santini, Italy</p><p>16:00 Michael Sherwood, USA</p><p>16:30 Poster Session 3</p><p class="in">with Coffee/Tea</p></div>
        <div class="blk"><p class="hd">Session 9: Pharmacological and Other Therapeutic Interventions in Stress and Aging Related Pathologies</p><p>17:30 Jane Treadwell, USA</p><p>18:00 N.N.</p><p>18:30 Short talk selected from abstracts</p><p>19:30-23:00 Cultural Program &amp; Banquet</p><p class="in">Dinner</p></div>
        <div class="blk"><p class="hd">Day 5. Thursday, August 17, 2017</p><p>09:00 Keynote 4</p><p class="in">(shared with the 27th Annual CellPark Turku Symposium "Checkpoints and Quality Control", CellPark Building)</p><p class="in">Peter Waldron, USA</p></div>
      </div>
    </div>
  </section>

  <div class="footer-rule"></div>
</main>
</body>
</html>
```